Business Card - Professional Minimalist - Double sided

We appreciate minimalist logo/web/collateral designs that allow design to tell a story. We want to relay a professional image/approach but throwing in a splash of modern when we’re able so long as it’s not distracting. Think 75% classic corporate, 25% modern. Open to black or white design, not sure which might look the best.

Target Market(s)

Senior executives or related government affairs contacts within the agriculture, energy, and defense industries (i.e., potential clients) but located outside of Washington, DC. Most potential clients based in DC with be familiar with both of us and our shared history.

Industry/Entity Type

Consulting

Contact Information for Business Card

Name: Daniel R. Whitlock
Title: Co-Founder & Partner
Address: 418 Bramblewood Ave. SE | Suite 2716 | Washington, D.C. 20019
Phone: (202) 555-0187
Email: Daniel@HollerbyWhitlock.com

Font styles to use
Serif

Colors

Designer to choose only greyscale colors for use in the design.

Requirements
Must have
• Name: Daniel R. Whitlock
Phone: (202) 555-0187

```html
<!DOCTYPE html>
<html lang="en">
<head>
<meta charset="utf-8">
<title>Hollerby Whitlock Group — Business Card</title>
<link rel="stylesheet" href="https://fonts.googleapis.com/css2?family=Cinzel:wght@400&family=Open+Sans:wght@400;700&display=swap">
<style>
  :root {
    --backdrop: #e4e4e4;
    --card-dark: #121212;
    --card-light: #f3f3f3;
    --brand-grey: #8c8c8c;
    --ink: #555555;
    --ink-dark: #2b2b2b;
    --rule: #9a9a9a;
  }
  html, body {
    margin: 0;
    width: 1200px;
    height: 960px;
    overflow: hidden;
    background: var(--backdrop);
  }
  .canvas { position: relative; width: 1200px; height: 960px; }
  .card { position: absolute; left: 310px; width: 583px; height: 332px; }
  .card--front { top: 122px; background: var(--card-dark); }
  .card--back { top: 506px; background: var(--card-light); }

  .brand {
    position: absolute; left: 0; right: 0; top: 146px;
    display: flex; align-items: center; justify-content: center; gap: 16px;
  }
  .brand__square { width: 36px; height: 36px; background: var(--brand-grey); }
  .brand__name {
    font-family: "Cinzel", serif; font-weight: 400; font-size: 28px;
    color: var(--brand-grey); letter-spacing: 0.5px;
  }

  .back__brand {
    position: absolute; left: 93px; top: 101px; width: 130px; height: 130px;
    display: flex; flex-direction: column; justify-content: center;
    font-family: "Cinzel", serif; font-size: 20px; line-height: 1.3;
    color: var(--ink);
  }
  .back__divider {
    position: absolute; left: 256px; top: 98px; width: 1px; height: 135px;
    background: var(--rule);
  }
  .person { position: absolute; left: 287px; top: 98px; font-family: "Open Sans", sans-serif; }
  .person__name { margin: 0; font-size: 18px; font-weight: 700; color: var(--ink); letter-spacing: 0.3px; }
  .person__title { margin: 2px 0 0; font-size: 14px; color: var(--ink); }
  .contacts { list-style: none; margin: 0; padding: 0; position: absolute; left: 287px; top: 174px;
    font-family: "Open Sans", sans-serif; font-size: 14px; color: var(--ink-dark); }
  .contacts li { display: flex; align-items: center; gap: 5px; height: 20px; }
  .contacts svg { width: 13px; height: 13px; fill: none; stroke: var(--ink); stroke-width: 1.5; }
  .address {
    position: absolute; left: 0; right: 0; top: 284px; margin: 0; text-align: center;
    font-family: "Open Sans", sans-serif; font-size: 14px; color: var(--ink-dark);
  }
</style>
</head>
<body>
<div class="canvas">
  <section class="card card--front">
    <div class="brand">
      <span class="brand__square"></span>
      <span class="brand__name">HOLLERBY WHITLOCK GROUP</span>
    </div>
  </section>

  <section class="card card--back">
    <div class="back__brand"><span>HOLLERBY</span><span>WHITLOCK</span></div>
    <div class="back__divider"></div>
    <div class="person">
      <h1 class="person__name">DANIEL R. WHITLOCK</h1>
      <p class="person__title">Co-Founder &amp; Partner</p>
    </div>
    <ul class="contacts">
      <li><svg viewBox="0 0 16 16"><path d="M3 2l3 0 1 3-2 1.5a8 8 0 0 0 4.5 4.5L11 9l3 1v3c0 1-1 1.5-2 1.5C6.5 14 2 9.5 1.5 4 1.5 3 2 2 3 2z" fill="#555" stroke="none"/></svg>(202) 555-0187</li>
      <li><svg viewBox="0 0 16 16"><rect x="1.5" y="3.5" width="13" height="9"/><path d="M1.5 3.5l6.5 5 6.5-5"/></svg>Daniel@HollerbyWhitlock.com</li>
      <li><svg viewBox="0 0 16 16"><circle cx="8" cy="8" r="6.5"/><ellipse cx="8" cy="8" rx="3" ry="6.5"/><path d="M1.5 8h13"/></svg>www.HollerbyWhitlock.com</li>
    </ul>
    <p class="address">418 Bramblewood Ave. SE | Suite 2716 | Washington, D.C. 20019</p>
  </section>
</div>
</body>
</html>
```